Trim Orchid - Weight management

Label for Weight management products.
Design: modern, clear, minimum design (less is more) – lifestyle product
Buyers: mainly female, young and middle age
I'm adding a number of blank labels for better understanding. The design should be made in a way that it looks like a product family. Because the weight management product series consist of about 10 products all together.

Target Market(s)

mainly female, young and middle age

Industry/Entity Type

Weight

Font styles to use
Sans Serif

Colors
e34297
0392cd
f37122

Requirements
Must have
• modern, clear, minimum design (less is more) – lifestyle product

```html
<!DOCTYPE html>
<html lang="en">
<head>
<meta charset="utf-8">
<title>Trim Orchid – Zinc Label</title>
<link rel="stylesheet" href="https://fonts.googleapis.com/css2?family=Saira+Condensed:wght@300;400&family=Montserrat:wght@600&display=swap">
<style>
  :root {
    --canvas: #ffffff;
    --band-deep: #c03a7d;
    --band-bright: #e34297;
    --label-dark: #231f20;
    --ink-light: #f2f2f2;
    --rule: #e6e6e6;
  }
  * { margin: 0; padding: 0; box-sizing: border-box; }
  html, body {
    width: 1200px;
    height: 1000px;
    overflow: hidden;
    background: var(--canvas);
  }
  .canvas {
    position: relative;
    width: 1200px;
    height: 1000px;
    background: var(--canvas);
  }
  .label {
    position: absolute;
    left: 276px;
    top: 128px;
    width: 648px;
    height: 745px;
  }
  .label-shape {
    position: absolute;
    inset: 0;
  }
  .brand {
    position: absolute;
    left: 0;
    width: 648px;
    top: 40px;
    display: flex;
    flex-direction: column;
    align-items: center;
    gap: 20px;
  }
  .brand-mark {
    width: 66px;
    height: 66px;
    border: 3px solid var(--ink-light);
    border-radius: 50%;
  }
  .brand-name {
    font-family: "Montserrat", sans-serif;
    font-weight: 600;
    font-size: 26px;
    letter-spacing: 5px;
    color: var(--ink-light);
    text-transform: uppercase;
  }
  .product-name {
    position: absolute;
    left: 90px;
    top: 298px;
    font-family: "Saira Condensed", sans-serif;
    font-weight: 300;
    font-size: 104px;
    line-height: 1;
    color: var(--ink-light);
  }
  .product-type, .fact {
    position: absolute;
    font-family: "Saira Condensed", sans-serif;
    font-weight: 400;
    color: var(--ink-light);
    text-align: center;
    line-height: 1;
  }
  .product-type {
    left: 48px;
    width: 552px;
    top: 572px;
    font-size: 42px;
  }
  .fact {
    top: 670px;
    font-size: 32px;
  }
  .fact--dose { left: 48px; width: 216px; }
  .fact--diet { left: 264px; width: 117px; }
  .fact--count { left: 381px; width: 219px; }
</style>
</head>
<body>
<main class="canvas">
  <section class="label" aria-label="Zinc supplement label">
    <svg class="label-shape" width="648" height="745" viewBox="0 0 648 745" aria-hidden="true">
      <defs>
        <linearGradient id="band-fill" x1="0" y1="0" x2="1" y2="0">
          <stop offset="0" stop-color="var(--band-deep)"/>
          <stop offset="1" stop-color="var(--band-bright)"/>
        </linearGradient>
      </defs>
      <rect x="0" y="0" width="648" height="745" fill="var(--label-dark)"/>
      <path d="M0 0 H648 V238 L0 250 Z" fill="url(#band-fill)"/>
      <path d="M150 248 L170 247.6 L162 268 Z" fill="var(--band-deep)"/>
      <g stroke="var(--rule)" stroke-width="2" fill="none">
        <line x1="48" y1="549" x2="600" y2="549"/>
        <line x1="48" y1="632" x2="600" y2="632"/>
        <line x1="264" y1="632" x2="264" y2="745"/>
        <line x1="381" y1="632" x2="381" y2="745"/>
      </g>
    </svg>

    <div class="brand">
      <span class="brand-mark" aria-hidden="true"></span>
      <span class="brand-name">Trim Orchid</span>
    </div>

    <h1 class="product-name">ZINC</h1>
    <p class="product-type">Essiential Mineral</p>
    <p class="fact fact--dose">One - A - day</p>
    <p class="fact fact--diet">Vegan</p>
    <p class="fact fact--count">90 Tablets</p>
  </section>
</main>
</body>
</html>
```